www.bluemarrowtours.example Weebly Web Design *with Coding*

I am looking for a fully operational Weebly design for www.bluemarrowtours.example that has the following:
1. Menus - I want the ability to have Multiple drop down menus.
2. E-commerce - The first iteration doesn't need to have e-commerce but the I might want that ability in the future.
3. Registration forms that can be filled out online. (I would give the fields that need to be filled out.)
4. Contracts that can be read and signed online that would be legally binding. (I would give the contract wording)
5. Pictures - Incorporates Professional Pictures that I have.
6. Site is offering Travel Services.
7. Logo - I already have a logo being developed elsewhere.
8. Domain Name - I already have the domain name secured and a temporary self-made site up that is built on Weebly.
9. I want to be able to take your design and do my own changes via Weebly.
10. Feel free to use any of the things you have already seen on the placeholder site I have up right now.
11. I want password protected pages that can only be accessed by a password.

Bright Fern Journey Advisors
www.bluemarrowtours.example

RE: Wire Frame

Home Page
Pictures
Short philosophy of Bright Fern Journey
Israel Trips
March 15-27, 2019 Itinerary
Places
Hotels
Day by Day
Pictures
March 30 – April 9, 2019
Places
Hotels
Day by Day
Pictures
Europe Trips
Italy
England
Ireland
About Us
Core Values and Mission
Founders
Pilgrimage vs. Trip
FAQ’s
General Information
Flights
Hotels
Inclusions/Exclusions to Cost
Payment Plans
Forms – Password Protected
Trip Questionnaire
Trip Contract
Legal
Bottom of Page Stuff

Target Market(s)

45 - 70 year olds looking to travel on custom guided tours.

Colors

Designer to choose colors to be used in the design.

Requirements
Must have
• 1. Ability to easily update the site.
• 2. Documents that can be filled out online and feed to me.
• 3. Great Flow - easy to navigate, easy drop down menus for more trips/pages.
• 4. Pictures that draw people in and want to travel with my company.
• 5. Clean look but not sterile.

```html
<!DOCTYPE html>
<html lang="en">
<head>
<meta charset="utf-8">
<title>Bright Fern Journey</title>
<link rel="stylesheet" href="https://fonts.googleapis.com/css2?family=Montserrat:wght@400;500;600;700&family=Open+Sans:wght@400;600;700&display=swap">
<style>
:root{
  --teal:#3b7f8f;
  --teal-dark:#2f6e7d;
  --ink:#1a1a1a;
  --body:#555;
  --pale:#e8f3f7;
  --line:#9fb8bd;
  --footer:#111;
  --white:#fff;
}
*{box-sizing:border-box;margin:0;padding:0}
html,body{width:1200px;height:2711px;overflow:hidden;background:var(--white)}
body{position:relative;font-family:"Open Sans",Arial,sans-serif;color:var(--ink)}
.abs{position:absolute}

/* hero */
.hero{left:0;top:0;width:1200px;height:600px;background:linear-gradient(180deg,#6c5a4e 0%,#8a6a52 12%,#5d5448 35%,#4a4238 60%,#3a3128 100%)}
.hero-glow{left:520px;top:390px;width:200px;height:140px;border-radius:50%;background:radial-gradient(ellipse,rgba(196,150,60,.55),rgba(196,150,60,0) 70%)}
.topbar{left:0;top:0;width:1200px;height:82px;border-bottom:1px solid rgba(255,255,255,.55);color:var(--white);font-family:"Montserrat",sans-serif}
.menu-btn{left:98px;top:0;height:82px;width:102px;border-right:1px solid rgba(255,255,255,.55);display:flex;align-items:center;gap:10px;font-weight:700;font-size:18px}
.brand{left:220px;top:0;height:82px;display:flex;align-items:center;font-weight:700;font-size:25px;letter-spacing:.5px}
.search-btn{left:1058px;top:0;width:70px;height:82px;border-left:1px solid rgba(255,255,255,.55);display:flex;align-items:center;justify-content:center}
.hero-title{left:0;top:190px;width:1200px;text-align:center;color:var(--white);font-family:"Montserrat",sans-serif;font-weight:700;font-size:66px;letter-spacing:1px}
.hero-sub{left:0;top:290px;width:1200px;text-align:center;color:var(--white);font-size:25px;line-height:40px}

/* packages */
.section-title{left:0;width:1200px;text-align:center;font-family:"Montserrat",sans-serif;font-weight:700;font-size:34px;color:var(--ink)}
.packages-intro{left:0;top:752px;width:1200px;text-align:center;font-family:"Montserrat",sans-serif;font-weight:500;font-size:24px;line-height:42px;color:#222}
.tour{top:887px;width:233px}
.tour-photo{width:233px;height:221px}
.tour-name{margin-top:37px;font-family:"Montserrat",sans-serif;font-weight:500;font-size:20px}
.tour-meta{margin-top:10px;display:flex;align-items:center;gap:6px;font-size:13px;color:#333}
.tour-meta .sep{margin:0 4px}
.price{color:var(--teal);font-weight:700;font-size:21px;display:flex;align-items:center;gap:3px}
.tour-desc{margin-top:12px;font-size:14px;line-height:23px;color:var(--body)}
.btn-outline{margin-top:24px;width:130px;height:46px;border:2px solid var(--teal);border-radius:23px;display:flex;align-items:center;justify-content:center;font-family:"Open Sans",sans-serif;font-weight:700;font-size:14px;color:var(--teal-dark)}
.btn-more{left:492px;top:1429px;width:215px;height:46px;border-radius:23px;background:var(--teal);color:var(--white);display:flex;align-items:center;justify-content:center;font-weight:700;font-size:15px}

/* featured */
.featured{left:0;top:1576px;width:1200px;height:510px;background:var(--pale)}
.feature{top:1764px;width:324px;height:238px;border:1.5px solid var(--line);text-align:center}
.feature-icon{position:absolute;left:119px;top:-43px;width:86px;height:86px;border-radius:50%;background:var(--teal);display:flex;align-items:center;justify-content:center}
.feature h3{margin-top:63px;font-family:"Montserrat",sans-serif;font-weight:500;font-size:21px}
.feature p{margin:14px auto 0;width:270px;font-size:14px;line-height:25px;color:var(--body)}
.feature .explore{margin-top:12px;font-weight:700;font-size:15px;color:var(--teal-dark)}

/* updates */
.updates{left:0;top:2086px;width:1200px;height:355px;background:linear-gradient(180deg,#5b97a3 0%,#4d8a97 55%,#4a8593 100%)}
.updates-title{left:0;top:2155px;width:1200px;text-align:center;color:var(--white);font-family:"Montserrat",sans-serif;font-weight:700;font-size:34px}
.updates-sub{left:0;top:2214px;width:1200px;text-align:center;color:var(--white);font-size:23px}
.signup{left:237px;top:2275px;width:726px;height:56px;border:2px solid var(--white);display:flex}
.signup-field{flex:1;display:flex;align-items:center;gap:10px;padding-left:16px;color:var(--white);font-size:14px}
.signup-btn{width:119px;background:var(--white);display:flex;align-items:center;justify-content:center;font-weight:700;font-size:17px;color:#111}

/* footer */
.footer{left:0;top:2441px;width:1200px;height:270px;background:var(--footer);color:var(--white)}
.social{top:2418px;width:50px;height:50px;border-radius:50%;background:var(--footer);border:2px solid var(--white);display:flex;align-items:center;justify-content:center}
.social .dot{width:12px;height:12px;border-radius:50%;background:var(--white)}
.contact{left:0;top:2504px;width:1200px;display:flex;justify-content:center;align-items:center;gap:14px;font-size:14px;color:var(--white)}
.contact span{display:flex;align-items:center;gap:8px}
.links{left:0;top:2546px;width:1200px;text-align:center;font-size:13px}
.copyright{left:0;top:2586px;width:1200px;text-align:center;font-size:14px}
.cards{left:483px;top:2634px;display:flex;gap:8px}
.cards i{display:block;width:42px;height:27px;border-radius:3px;background:#6b6b6b}
</style>
</head>
<body>

<div class="abs hero" role="img" aria-label="Evening view over the rooftops of Jerusalem with a golden dome in the centre"></div>
<div class="abs hero-glow"></div>

<header class="abs topbar">
  <div class="abs menu-btn">
    <svg width="16" height="14" viewBox="0 0 16 14"><rect y="0" width="16" height="2.4" fill="#fff"/><rect y="5.8" width="16" height="2.4" fill="#fff"/><rect y="11.6" width="16" height="2.4" fill="#fff"/></svg>
    MENU
  </div>
  <div class="abs brand">BRIGHT FERN JOURNEY</div>
  <div class="abs search-btn">
    <svg width="18" height="18" viewBox="0 0 18 18"><circle cx="7.5" cy="7.5" r="5.5" fill="none" stroke="#fff" stroke-width="2.4"/><line x1="11.5" y1="11.5" x2="16.5" y2="16.5" stroke="#fff" stroke-width="2.6" stroke-linecap="round"/></svg>
  </div>
</header>

<h1 class="abs hero-title">BRIGHT FERN JOURNEY</h1>
<p class="abs hero-sub">Come travel with Bright Fern Journey and make your<br>own extraordinary memories in the Holy Land of Israel</p>

<h2 class="abs section-title" style="top:684px">TOUR PACKAGES</h2>
<p class="abs packages-intro">These things come together on a trip to the Holy Land. We have led<br>groups all over the world including trips throughout</p>

<article class="abs tour" style="left:99px">
  <div class="tour-photo" role="img" aria-label="Old city walls and golden dome lit at dusk" style="background:linear-gradient(180deg,#1f3f8a 0%,#3b63b5 45%,#c9b58a 75%,#8e7a5c 100%)"></div>
  <div class="tour-name">Holy Land</div>
  <div class="tour-meta"><svg width="11" height="11" viewBox="0 0 12 12"><circle cx="6" cy="6" r="5" fill="none" stroke="#3b7f8f" stroke-width="1.6"/><path d="M6 3v3.2l2 1.3" fill="none" stroke="#3b7f8f" stroke-width="1.4"/></svg>12 Days 11 Nights<span class="sep">|</span><span class="price">$1350<svg width="14" height="14" viewBox="0 0 14 14"><path d="M1 1h6l6 6-6 6-6-6z" fill="#3b7f8f"/><circle cx="4" cy="4" r="1.2" fill="#fff"/></svg></span></div>
  <p class="tour-desc">Nemo enim ipsam voluptatem quia voluptas sit aspernatur aut odit aut fugit, sed quia consequ..</p>
  <div class="btn-outline">BUY NOW!</div>
</article>

<article class="abs tour" style="left:356px">
  <div class="tour-photo" role="img" aria-label="Domed church among terracotta rooftops under a blue sky" style="background:linear-gradient(180deg,#7fb0dc 0%,#b9c7cf 35%,#a9866a 65%,#8a5b3e 100%)"></div>
  <div class="tour-name">Holy Land</div>
  <div class="tour-meta"><svg width="11" height="11" viewBox="0 0 12 12"><circle cx="6" cy="6" r="5" fill="none" stroke="#3b7f8f" stroke-width="1.6"/><path d="M6 3v3.2l2 1.3" fill="none" stroke="#3b7f8f" stroke-width="1.4"/></svg>12 Days 11 Nights<span class="sep">|</span><span class="price">$1350<svg width="14" height="14" viewBox="0 0 14 14"><path d="M1 1h6l6 6-6 6-6-6z" fill="#3b7f8f"/><circle cx="4" cy="4" r="1.2" fill="#fff"/></svg></span></div>
  <p class="tour-desc">Nemo enim ipsam voluptatem quia voluptas sit aspernatur aut odit aut fugit, sed quia consequ..</p>
  <div class="btn-outline">BUY NOW!</div>
</article>

<article class="abs tour" style="left:613px">
  <div class="tour-photo" role="img" aria-label="Harbour town with colourful boats and golden stone buildings" style="background:linear-gradient(180deg,#3f7fcf 0%,#7aaee0 30%,#d9a54a 55%,#c0542e 75%,#2a6fa0 100%)"></div>
  <div class="tour-name">Holy Land</div>
  <div class="tour-meta"><svg width="11" height="11" viewBox="0 0 12 12"><circle cx="6" cy="6" r="5" fill="none" stroke="#3b7f8f" stroke-width="1.6"/><path d="M6 3v3.2l2 1.3" fill="none" stroke="#3b7f8f" stroke-width="1.4"/></svg>12 Days 11 Nights<span class="sep">|</span><span class="price">$1350<svg width="14" height="14" viewBox="0 0 14 14"><path d="M1 1h6l6 6-6 6-6-6z" fill="#3b7f8f"/><circle cx="4" cy="4" r="1.2" fill="#fff"/></svg></span></div>
  <p class="tour-desc">Nemo enim ipsam voluptatem quia voluptas sit aspernatur aut odit aut fugit, sed quia consequ..</p>
  <div class="btn-outline">BUY NOW!</div>
</article>

<article class="abs tour" style="left:869px">
  <div class="tour-photo" role="img" aria-label="Sun rays breaking through clouds over the city skyline" style="background:linear-gradient(180deg,#1d3f8c 0%,#3d64a8 35%,#e7c35a 55%,#8a7a52 75%,#4e4a3a 100%)"></div>
  <div class="tour-name">Holy Land</div>
  <div class="tour-meta"><svg width="11" height="11" viewBox="0 0 12 12"><circle cx="6" cy="6" r="5" fill="none" stroke="#3b7f8f" stroke-width="1.6"/><path d="M6 3v3.2l2 1.3" fill="none" stroke="#3b7f8f" stroke-width="1.4"/></svg>12 Days 11 Nights<span class="sep">|</span><span class="price">$1350<svg width="14" height="14" viewBox="0 0 14 14"><path d="M1 1h6l6 6-6 6-6-6z" fill="#3b7f8f"/><circle cx="4" cy="4" r="1.2" fill="#fff"/></svg></span></div>
  <p class="tour-desc">Nemo enim ipsam voluptatem quia voluptas sit aspernatur aut odit aut fugit, sed quia consequ..</p>
  <div class="btn-outline">BUY NOW!</div>
</article>

<div class="abs btn-more">VIEW MORE PACKAGE</div>

<section class="abs featured"></section>
<h2 class="abs section-title" style="top:1627px">FEATURED</h2>

<div class="abs feature" style="left:99px">
  <div class="feature-icon"><svg width="38" height="38" viewBox="0 0 38 38"><rect x="4" y="7" width="30" height="27" rx="3" fill="none" stroke="#fff" stroke-width="3"/><line x1="4" y1="14" x2="34" y2="14" stroke="#fff" stroke-width="3"/><line x1="12" y1="3" x2="12" y2="10" stroke="#fff" stroke-width="3"/><line x1="26" y1="3" x2="26" y2="10" stroke="#fff" stroke-width="3"/><g fill="#fff"><rect x="9" y="18" width="5" height="4"/><rect x="16.5" y="18" width="5" height="4"/><rect x="24" y="18" width="5" height="4"/><rect x="9" y="25" width="5" height="4"/><rect x="16.5" y="25" width="5" height="4"/><rect x="24" y="25" width="5" height="4"/></g></svg></div>
  <h3>Daily Tours</h3>
  <p>Nemo enim ipsam voluptatem quia voluptas sit aspernatur aut odit aut fugit, sed quia consequuntur magni</p>
  <div class="explore">EXPLORE MORE</div>
</div>

<div class="abs feature" style="left:438px">
  <div class="feature-icon"><svg width="40" height="40" viewBox="0 0 40 40"><path d="M4 4h14l18 18-14 14L4 18z" fill="#fff"/><circle cx="11" cy="11" r="3" fill="#3b7f8f"/></svg></div>
  <h3>Package Tours</h3>
  <p>Nemo enim ipsam voluptatem quia voluptas sit aspernatur aut odit aut fugit, sed quia consequuntur magni</p>
  <div class="explore">EXPLORE MORE</div>
</div>

<div class="abs feature" style="left:777px">
  <div class="feature-icon"><svg width="36" height="38" viewBox="0 0 36 38"><circle cx="18" cy="11" r="8" fill="#fff"/><path d="M2 36c0-9 7-15 16-15s16 6 16 15z" fill="#fff"/></svg></div>
  <h3>Private Tours</h3>
  <p>Nemo enim ipsam voluptatem quia voluptas sit aspernatur aut odit aut fugit, sed quia consequuntur magni</p>
  <div class="explore">EXPLORE MORE</div>
</div>

<section class="abs updates" role="img" aria-label="Teal-toned view of the old city walls and plaza"></section>
<h2 class="abs updates-title">GET FREE UPDATES</h2>
<p class="abs updates-sub">Register your email address to&nbsp; get free updates</p>
<form class="abs signup">
  <div class="signup-field"><svg width="14" height="11" viewBox="0 0 14 11"><rect width="14" height="11" rx="1" fill="#fff"/><path d="M0.5 1l6.5 5 6.5-5" fill="none" stroke="#4d8a97" stroke-width="1.4"/></svg>Email Address</div>
  <div class="signup-btn">SIGN UP</div>
</form>

<footer class="abs footer"></footer>
<div class="abs social" style="left:488px"><span class="dot"></span></div>
<div class="abs social" style="left:546px"><span class="dot"></span></div>
<div class="abs social" style="left:604px"><span class="dot"></span></div>
<div class="abs social" style="left:662px"><svg width="18" height="14" viewBox="0 0 18 14"><rect width="18" height="14" rx="2" fill="#fff"/><path d="M1 1.5l8 6 8-6" fill="none" stroke="#111" stroke-width="1.6"/></svg></div>

<div class="abs contact">
  <span><svg width="11" height="15" viewBox="0 0 11 15"><path d="M5.5 0C2.5 0 0 2.4 0 5.4 0 9.4 5.5 15 5.5 15S11 9.4 11 5.4C11 2.4 8.5 0 5.5 0z" fill="#fff"/><circle cx="5.5" cy="5.4" r="2" fill="#111"/></svg>214 Willow Crest Road, Suite 12, Springvale, TX 75000</span>
  <span>|</span>
  <span><svg width="14" height="14" viewBox="0 0 14 14"><path d="M3 0l3 3-1.6 2a8 8 0 0 0 4.6 4.6L11 8l3 3-2 3C5.5 14 0 8.5 0 2z" fill="#fff"/></svg>1 800 555 0142</span>
  <span>|</span>
  <span><svg width="15" height="11" viewBox="0 0 15 11"><rect width="15" height="11" rx="1" fill="#fff"/><path d="M0.5 1l7 5 7-5" fill="none" stroke="#111" stroke-width="1.4"/></svg>hello@brightfernjourney.example</span>
</div>
<nav class="abs links">Help &nbsp;|&nbsp; FAQ &nbsp;|&nbsp; Support &nbsp;|&nbsp; Sitemap &nbsp;|&nbsp; Terms Of Use &nbsp;|&nbsp; Privacy Statement</nav>
<p class="abs copyright">Copyrights © 2018, Bright Fern Journey. All rights reserved.</p>
<div class="abs cards" aria-label="Accepted payment methods"><i></i><i></i><i></i><i></i><i></i></div>

</body>
</html>
```